iPhone iOS 7 App For Managing Tasks/Photos for Internal Company Use

We need an app design that displays company objectives and task, and provides the interface for employees to complete a task by uploading a photo and adding comments.

Please see attached mock up sketches as a rough guideline

Final delivery of files must contain PSD, and all layers/objects sliced both is PSD and PNG files

Target Market(s)

This is a tool for internal employee use

Industry/Entity Type

It Company

Requirements
Must have
• Must include logo, and match the colour scheme
Use iPhone iOS 7 Style

```html
<!DOCTYPE html>
<html lang="en">
<head>
<meta charset="utf-8">
<title>Staff Tasks – Login</title>
<link href="https://fonts.googleapis.com/css2?family=Arimo:wght@400;700&display=swap" rel="stylesheet">
<style>
  :root{
    --bar-dark:#0b0b0b;
    --bar-mid:#2a2a2a;
    --sea-top:#0f4f6e;
    --sea-mid:#0a3a57;
    --sea-deep:#06223a;
    --white:#ffffff;
    --field-bg:#f4f4f4;
    --field-border:#b9b9b9;
    --hint:#a9a9a9;
    --ok:#3aa62a;
    --err:#c4201c;
    --btn-top:#3a3a3a;
    --btn-bottom:#0e0e0e;
    --tab-bg:#121212;
    --home:#e8701c;
    --target:#7a1d12;
    --news:#1f3f8c;
    --logout:#d91f1a;
  }
  *{box-sizing:border-box;margin:0;padding:0}
  html,body{width:800px;height:1200px;overflow:hidden;background:#000}
  body{font-family:"Arimo",Arial,sans-serif;position:relative}
  .status-bar{position:absolute;left:0;top:0;width:800px;height:50px;
    background:linear-gradient(var(--bar-mid),var(--bar-dark));color:var(--white);
    font-size:36px;display:flex;align-items:center;justify-content:center}
  .status-bar .signal{position:absolute;left:12px;top:10px}
  .status-bar .battery{position:absolute;right:12px;top:11px}
  .backdrop{position:absolute;left:0;top:50px;width:800px;height:995px;
    background:radial-gradient(ellipse at 35% 25%,#1c6c8c 0%,var(--sea-top) 30%,var(--sea-mid) 65%,var(--sea-deep) 100%)}
  .field-label{position:absolute;left:0;width:800px;text-align:center;color:var(--white);
    font-weight:700;font-size:55px}
  .label-user{top:243px}
  .label-pass{top:483px}
  .field{position:absolute;left:110px;width:590px;height:80px;background:var(--field-bg);
    border:2px solid var(--field-border);border-radius:4px;display:flex;align-items:center;padding-left:18px}
  .field-user{top:332px}
  .field-pass{top:567px}
  .field-user .value{color:var(--hint);font-size:40px}
  .field-pass .value{color:#111;font-size:48px;letter-spacing:6px;line-height:1}
  .field .state{position:absolute;right:14px;top:24px}
  .login-btn{position:absolute;left:252px;top:715px;width:266px;height:90px;border-radius:22px;
    background:linear-gradient(var(--btn-top),var(--btn-bottom));border:3px solid #5a5a5a;
    box-shadow:0 4px 10px rgba(0,0,0,.5);display:flex;align-items:center;justify-content:center;gap:16px;
    color:var(--white);font-weight:700;font-size:40px}
  .tab-bar{position:absolute;left:0;top:1045px;width:800px;height:155px;background:var(--tab-bg);
    border-top:2px solid #2b2b2b}
  .tab{position:absolute;top:12px;width:200px;margin-left:-100px;text-align:center;color:var(--white);
    font-weight:700;font-size:30px}
  .tab svg{display:block;margin:0 auto 10px}
</style>
</head>
<body>
  <header class="status-bar">
    <svg class="signal" width="70" height="30" viewBox="0 0 70 30">
      <rect x="0" y="22" width="9" height="8" fill="#fff"/>
      <rect x="13" y="17" width="9" height="13" fill="#fff"/>
      <rect x="26" y="12" width="9" height="18" fill="#fff"/>
      <rect x="39" y="6" width="9" height="24" fill="#fff"/>
      <rect x="52" y="0" width="9" height="30" fill="#fff"/>
    </svg>
    <span class="clock">9:20 AM</span>
    <svg class="battery" width="62" height="28" viewBox="0 0 62 28">
      <rect x="1" y="1" width="54" height="26" rx="4" fill="none" stroke="#fff" stroke-width="2"/>
      <rect x="5" y="5" width="46" height="18" rx="2" fill="#fff"/>
      <rect x="56" y="9" width="5" height="10" fill="#fff"/>
    </svg>
  </header>

  <main class="backdrop" role="img" aria-label="Dark blue background photo of rain drops on glass"></main>

  <div class="field-label label-user">Username</div>
  <div class="field field-user">
    <span class="value">mara_lenton</span>
    <svg class="state" width="32" height="32" viewBox="0 0 32 32">
      <circle cx="16" cy="16" r="15" fill="var(--ok)"/>
      <path d="M9 16l5 5 9-10" fill="none" stroke="#fff" stroke-width="4" stroke-linecap="round"/>
    </svg>
  </div>

  <div class="field-label label-pass">Password</div>
  <div class="field field-pass">
    <span class="value">●●●●●●●</span>
    <svg class="state" width="32" height="32" viewBox="0 0 32 32">
      <circle cx="16" cy="16" r="15" fill="var(--err)"/>
      <path d="M10 10l12 12M22 10L10 22" stroke="#fff" stroke-width="4" stroke-linecap="round"/>
    </svg>
  </div>

  <div class="login-btn">
    <svg width="50" height="56" viewBox="0 0 50 56">
      <path d="M12 26V17a13 13 0 0 1 26 0v9" fill="none" stroke="#c9c9c9" stroke-width="6"/>
      <rect x="4" y="25" width="42" height="30" rx="4" fill="#f2b520"/>
      <circle cx="25" cy="38" r="4" fill="#8a5a00"/>
      <rect x="23" y="40" width="4" height="8" fill="#8a5a00"/>
    </svg>
    <span>Login »</span>
  </div>

  <nav class="tab-bar">
    <div class="tab" style="left:88px">
      <svg width="90" height="90" viewBox="0 0 90 90">
        <rect x="2" y="2" width="86" height="86" rx="12" fill="var(--home)"/>
        <path d="M20 46L45 22l25 24" fill="none" stroke="#fff" stroke-width="7" stroke-linejoin="round"/>
        <path d="M27 44v26h14V56h8v14h14V44L45 27z" fill="#fff"/>
      </svg>Home
    </div>
    <div class="tab" style="left:290px">
      <svg width="90" height="90" viewBox="0 0 90 90">
        <rect x="2" y="2" width="86" height="86" rx="12" fill="var(--target)" stroke="#b48a3a" stroke-width="3"/>
        <circle cx="45" cy="45" r="30" fill="#fff"/>
        <circle cx="45" cy="45" r="23" fill="#d12a1c"/>
        <circle cx="45" cy="45" r="15" fill="#fff"/>
        <circle cx="45" cy="45" r="8" fill="#d12a1c"/>
        <path d="M45 45L74 18" stroke="#333" stroke-width="4"/>
      </svg>Objective
    </div>
    <div class="tab" style="left:500px">
      <svg width="90" height="90" viewBox="0 0 90 90">
        <rect x="2" y="2" width="86" height="86" rx="12" fill="var(--news)" stroke="#c9c9c9" stroke-width="3"/>
        <circle cx="45" cy="40" r="24" fill="#2f8fe0" stroke="#fff" stroke-width="3"/>
        <ellipse cx="45" cy="40" rx="10" ry="24" fill="none" stroke="#fff" stroke-width="3"/>
        <path d="M21 40h48" stroke="#fff" stroke-width="3"/>
        <rect x="22" y="68" width="46" height="14" fill="#fff"/>
      </svg>News
    </div>
    <div class="tab" style="left:708px">
      <svg width="90" height="90" viewBox="0 0 90 90">
        <rect x="2" y="2" width="86" height="86" rx="14" fill="var(--logout)"/>
        <path d="M31 28a24 24 0 1 0 28 0" fill="none" stroke="#fff" stroke-width="8" stroke-linecap="round"/>
        <path d="M45 16v30" stroke="#fff" stroke-width="8" stroke-linecap="round"/>
      </svg>Logout
    </div>
  </nav>
</body>
</html>
```